(LUMO PEAK ADVISORY SERVICE) Credit Repair Service

We are committed to customer service, Credit Repair Service, Consumer Finance, Landlord Tenant, Traffic, Estate Planning, Collection, Family Law, Civil Litigation, and so much more.

Vento Crest Prime Payment plans starting at $200 per month

Consumer Finance, Landlord Tenant, Traffic, Estate Planning, Collection, Family Law, Civil Litigation, and so much more

Credit Services

Tandem Orivex $1,700

One-on-One consultations with a Certified KURT© Professional

Bureau Challenges

Creditor Interventions

Inquiry Assist

Score Analysis

Report Watch

Crediway® Alerts

Cease & Desist Letters

KURT® Rating Monitor

Identity Protection

Personal Finance Tools

Tandem Amber $1,400

Bureau Challenges

Creditor Interventions

Inquiry Assist

Score Analysis

Report Watch

Crediway® Alerts

Tandem Copper $,1150

Bureau Challenges

Creditor Interventions

Industry/Entity Type

Consulting

Coding

Coded - Design and coding required

Number of Pages Required

1 page

Colors
cee9f5
85cae6
ecf7fb

Requirements
Must have
• We are committed to customer service, Credit Repair Service, Consumer Finance, Landlord Tenant, Traffic, Estate Planning, Collection, Family Law, Civil Litigation, and so much more.
• Vento Crest Prime Payment plans starting at $200 per month
• Consumer Finance, Landlord Tenant, Traffic, Estate Planning, Collection, Family Law, Civil Litigation, and so much more
• Credit Services
• Tandem Orivex $1,700
• One-on-One consultations with a Certified KURT© Professional
• Bureau Challenges
• Creditor Interventions
• Inquiry Assist
• Score Analysis
• Report Watch
• Crediway® Alerts
• Cease & Desist Letters
• KURT® Rating Monitor
• Identity Protection
• Personal Finance Tools
• Tandem Amber $1,400
• Bureau Challenges
• Creditor Interventions
• Inquiry Assist
• Score Analysis
• Report Watch
• Crediway® Alerts
• Tandem Copper $,1150
• Bureau Challenges
• Creditor Interventions
• Pricing, services, about us, generic pictures, contact information,
• Contact information -( wilma82dun@postnest.example) 4712 SE 215 Avenue Miami FL 33190
Nice to have

```html
<!DOCTYPE html>
<html lang="en">
<head>
<meta charset="utf-8">
<title>Lumo Peak Advisory – Credit Repair Service</title>
<link href="https://fonts.googleapis.com/css2?family=Raleway:wght@400;500;600&family=Open+Sans:wght@400;600&family=Roboto+Slab:wght@300;400&display=swap" rel="stylesheet">
<style>
:root{
  --blue:#6dbde0;
  --blue-mid:#85cae6;
  --blue-pale:#cee9f5;
  --blue-wash:#ecf7fb;
  --heading-blue:#62b6dc;
  --ink:#333;
  --body:#666;
  --line:#e7e7e7;
  --grey-bg:#f5f5f5;
  --navy:#10294a;
  --white:#fff;
}
*{margin:0;padding:0;box-sizing:border-box}
html,body{width:1200px;height:2899px;overflow:hidden;background:var(--white)}
body{position:relative;font-family:'Open Sans',Arial,sans-serif;color:var(--ink)}
.abs{position:absolute}

/* header */
.top-rule{left:0;top:0;width:1200px;height:4px;background:var(--blue)}
.site-header{left:0;top:4px;width:1200px;height:96px;background:var(--white);border-bottom:1px solid var(--line)}
.brand{left:85px;top:30px;font-family:'Roboto Slab',Georgia,serif;font-weight:300;font-size:27px;color:var(--heading-blue)}
.nav{top:40px;font-family:'Raleway',Arial,sans-serif;font-size:12.5px;font-weight:600;color:#333;letter-spacing:.3px}
.nav.active{color:var(--heading-blue)}
.search{left:1064px;top:24px;width:48px;height:48px;border:2px solid var(--blue);border-radius:50%}
.search svg{position:absolute;left:14px;top:14px}

/* hero */
.hero{left:0;top:100px;width:1200px;height:542px;background:linear-gradient(90deg,#f2f3f3 0%,#e9ecec 40%,#c9c2bb 60%,#a48e7e 75%,#d8d2cc 100%)}
.hero-title{left:85px;top:246px;font-family:'Raleway',Arial,sans-serif;font-size:30px;font-weight:500;color:#2b2b2b}
.hero-sub{left:85px;top:303px;font-family:'Raleway',Arial,sans-serif;font-size:26px;line-height:40px;color:var(--heading-blue)}
.hero-sub strong{color:#3a3a3a;font-weight:600}
.btn{display:flex;align-items:center;justify-content:center;background:var(--blue);color:var(--white);border-radius:24px;font-family:'Raleway',Arial,sans-serif;font-size:13px;font-weight:600;letter-spacing:.5px}
.hero-btn{left:85px;top:408px;width:118px;height:42px;font-size:12px}

/* grey band */
.grey-band{left:0;top:642px;width:1200px;height:1566px;background:var(--grey-bg)}

/* what we do */
.services-card{left:86px;top:573px;width:1028px;height:705px;background:var(--white);border:1px solid #ddd;box-shadow:0 1px 4px rgba(0,0,0,.08)}
.section-title{width:100%;text-align:center;font-family:'Raleway',Arial,sans-serif;font-size:31px;font-weight:500;color:var(--heading-blue)}
.section-intro{text-align:center;font-size:12px;line-height:25px;color:var(--body)}
.service{width:300px;text-align:center}
.service svg{display:block;margin:0 auto}
.service h3{margin-top:16px;font-family:'Raleway',Arial,sans-serif;font-size:16px;font-weight:600;color:#2d2d2d}
.service p{margin-top:14px;font-size:12px;line-height:25px;color:var(--body)}
.view-more{left:518px;top:1191px;width:164px;height:44px}

/* pricing */
.plan{top:1453px;width:299px;height:702px;background:var(--white);border:1px solid #e2e2e2}
.plan-head{height:96px;background:var(--blue);text-align:center;padding-top:21px;font-family:'Raleway',Arial,sans-serif;font-size:17px;font-weight:600;color:var(--white);letter-spacing:.3px}
.price{position:absolute;left:94px;top:55px;width:110px;height:110px;border-radius:50%;background:var(--white);border:5px solid var(--blue-pale);box-shadow:0 0 0 1px var(--blue-mid) inset;display:flex;align-items:center;justify-content:center;font-family:'Open Sans',Arial,sans-serif;font-size:24px;font-weight:600;color:#4897bf}
.plan-note{margin-top:74px;padding:0 20px 10px;text-align:center;font-size:12.5px;line-height:25px;color:var(--heading-blue)}
.plan ul{list-style:none;border-top:1px solid var(--line)}
.plan li{height:38.7px;line-height:38px;text-align:center;font-size:13.5px;color:#444;border-bottom:1px solid var(--line)}
.plan .btn{position:absolute;left:85px;top:637px;width:128px;height:40px}

/* about */
.about-visual{left:150px;top:2305px;width:355px;height:295px;border-radius:12px;background:linear-gradient(135deg,#9fb3c9 0%,#d9c07a 40%,#e08a4a 60%,#5a8fc8 100%)}
.about-title{left:545px;top:2268px;font-family:'Raleway',Arial,sans-serif;font-size:31px;font-weight:500;color:var(--heading-blue)}
.about-copy{left:545px;width:535px;font-size:12px;line-height:26px;color:var(--body)}

/* footer */
.site-footer{left:0;top:2634px;width:1200px;height:265px;background:var(--navy);color:var(--white)}
.footer-brand{left:0;top:24px;width:1200px;text-align:center;font-family:'Roboto Slab',Georgia,serif;font-weight:300;font-size:33px}
.footer-rule{left:0;top:93px;width:1200px;height:1px;background:rgba(255,255,255,.12)}
.contact{top:120px;display:flex;align-items:center;gap:16px}
.contact-icon{width:54px;height:54px;border:2px solid rgba(255,255,255,.85);border-radius:50%;display:flex;align-items:center;justify-content:center;flex:none}
.contact h4{font-family:'Raleway',Arial,sans-serif;font-size:18px;font-weight:600}
.contact p{font-size:12px;margin-top:4px}
.copyright{left:0;top:224px;width:1200px;text-align:center;font-size:12px}
</style>
</head>
<body>

<div class="abs top-rule"></div>
<header class="abs site-header">
  <div class="abs brand">Lumo Peak Advisory</div>
  <span class="abs nav active" style="left:549px">HOME</span>
  <span class="abs nav" style="left:642px">PRICING</span>
  <span class="abs nav" style="left:747px">SERVICES</span>
  <span class="abs nav" style="left:860px">ABOUT US</span>
  <span class="abs nav" style="left:978px">CONTACT US</span>
  <div class="abs search"><svg width="16" height="16" viewBox="0 0 16 16" fill="none" stroke="#6dbde0" stroke-width="2.4"><circle cx="6.5" cy="6.5" r="4.5"/><path d="M10 10l4 4"/></svg></div>
</header>

<section class="abs hero" role="img" aria-label="Photo of a smiling couple at a laptop holding a payment card in a bright room"></section>
<h1 class="abs hero-title">CREDIT REPAIR SERVICE</h1>
<p class="abs hero-sub">Vento Crest Prime Payment plans<br>starting at <strong>$200 PER MONTH</strong></p>
<a class="abs btn hero-btn">READ MORE</a>

<div class="abs grey-band"></div>

<section class="abs services-card">
  <h2 class="abs section-title" style="top:36px">WHAT WE DO</h2>
  <p class="abs section-intro" style="left:0;top:84px;width:1028px">Sed ut perspiciatis unde omnis iste natus error sit voluptatem accusantium doloremque laudantium, totam rem aperiam, eaque ipsa quae ab<br>illo inventore veritatis et quasi architecto beatae vitae dicta sunt explicabo.</p>

  <div class="abs service" style="left:21px;top:200px">
    <svg width="64" height="60" viewBox="0 0 64 60" fill="none" stroke="#6dbde0" stroke-width="2.5"><path d="M14 32a18 18 0 0 1 36 0"/><rect x="9" y="30" width="8" height="14" rx="3" fill="#6dbde0"/><rect x="47" y="30" width="8" height="14" rx="3" fill="#6dbde0"/><circle cx="32" cy="32" r="13"/><path d="M14 58c2-9 9-12 18-12s16 3 18 12"/></svg>
    <h3>CUSTOMER SERVICE</h3>
    <p>Sed ut perspiciatis unde omnis iste natus error sit<br>rem aperiam, eaque ipsa quae ab</p>
  </div>
  <div class="abs service" style="left:364px;top:200px">
    <svg width="64" height="60" viewBox="0 0 64 60" fill="none" stroke="#6dbde0" stroke-width="2.5"><rect x="12" y="16" width="40" height="28" rx="2"/><path d="M4 48h56l-4 5H8z"/><circle cx="32" cy="30" r="6"/><path d="M32 20v4M32 36v4M22 30h4M38 30h4"/></svg>
    <h3>CREDIT REPAIR SERVICE</h3>
    <p>Sed ut perspiciatis unde omnis iste natus error sit<br>rem aperiam, eaque ipsa quae ab</p>
  </div>
  <div class="abs service" style="left:707px;top:200px">
    <svg width="64" height="60" viewBox="0 0 64 60"><path d="M25 6h14l-4 9h-6z" fill="#6dbde0"/><path d="M28 17h8c12 6 16 18 14 28-1 8-8 11-18 11s-17-3-18-11c-2-10 2-22 14-28z" fill="#6dbde0"/><text x="32" y="46" text-anchor="middle" font-family="Arial,sans-serif" font-size="22" font-weight="700" fill="#fff">$</text></svg>
    <h3>CONSUMER FINANCE</h3>
    <p>Sed ut perspiciatis unde omnis iste natus error sit<br>rem aperiam, eaque ipsa quae ab</p>
  </div>

  <div class="abs service" style="left:21px;top:410px">
    <svg width="64" height="60" viewBox="0 0 64 60" fill="none" stroke="#6dbde0" stroke-width="2.5"><path d="M22 24l12-10 12 10v14H22z"/><rect x="30" y="28" width="8" height="10"/><path d="M10 44h14l10 6 14-8M10 54h28l18-12"/></svg>
    <h3>LANDLORD TENANT</h3>
    <p>Sed ut perspiciatis unde omnis iste natus error sit<br>rem aperiam, eaque ipsa quae ab</p>
  </div>
  <div class="abs service" style="left:364px;top:410px">
    <svg width="64" height="60" viewBox="0 0 64 60" fill="none" stroke="#6dbde0" stroke-width="2.5"><rect x="22" y="4" width="20" height="52" rx="4"/><circle cx="32" cy="15" r="5"/><circle cx="32" cy="30" r="5"/><circle cx="32" cy="45" r="5"/><path d="M22 12h-8l8 8M22 27h-8l8 8M42 12h8l-8 8M42 27h8l-8 8"/></svg>
    <h3>TRAFFIC</h3>
    <p>Sed ut perspiciatis unde omnis iste natus error sit<br>rem aperiam, eaque ipsa quae ab</p>
  </div>
  <div class="abs service" style="left:707px;top:410px">
    <svg width="64" height="60" viewBox="0 0 64 60" fill="none" stroke="#6dbde0" stroke-width="2.5"><path d="M10 54V10h36v44M6 54h52"/><path d="M16 18h6M16 26h6M16 34h6M28 18h6M28 26h6"/><path d="M30 44l12-10 12 10v10H30z"/><rect x="38" y="46" width="6" height="8"/></svg>
    <h3>ESTATE PLANNING</h3>
    <p>Sed ut perspiciatis unde omnis iste natus error sit<br>rem aperiam, eaque ipsa quae ab</p>
  </div>
</section>
<a class="abs btn view-more">VIEW MORE</a>

<h2 class="abs section-title" style="left:0;top:1326px">CREDIT SERVICES</h2>
<p class="abs section-intro" style="left:0;top:1376px;width:1200px">Sed ut perspiciatis unde omnis iste natus error sit voluptatem accusantium doloremque laudantium, totam rem aperiam</p>

<article class="abs plan" style="left:124px">
  <div class="plan-head">TANDEM ORIVEX</div>
  <div class="price">$1,700</div>
  <p class="plan-note">One-on-One consultations with a Certified KURT© Professional</p>
  <ul>
    <li>Bureau Challenges</li><li>Creditor Interventions</li><li>Inquiry Assist</li><li>Score Analysis</li><li>Report Watch</li><li>Crediway® Alerts</li><li>Cease &amp; Desist Letters</li><li>KURT® Rating Monitor</li><li>Identity Protection</li><li>Personal Finance Tools</li>
  </ul>
  <a class="btn">SIGNUP</a>
</article>

<article class="abs plan" style="left:447px">
  <div class="plan-head">TANDEM AMBER</div>
  <div class="price">$1,400</div>
  <p class="plan-note">One-on-One consultations with a Certified KURT© Professional</p>
  <ul>
    <li>Bureau Challenges</li><li>Creditor Interventions</li><li>Inquiry Assist</li><li>Score Analysis</li><li>Report Watch</li><li>Crediway® Alerts</li>
  </ul>
  <a class="btn">SIGNUP</a>
</article>

<article class="abs plan" style="left:771px">
  <div class="plan-head">TANDEM COPPER</div>
  <div class="price">$,1150</div>
  <p class="plan-note">One-on-One consultations with a Certified KURT© Professional</p>
  <ul>
    <li>Bureau Challenges</li><li>Creditor Interventions</li>
  </ul>
  <a class="btn">SIGNUP</a>
</article>

<div class="abs about-visual" role="img" aria-label="Fanned stack of colourful payment cards"></div>
<h2 class="abs about-title">ABOUT US</h2>
<p class="abs about-copy" style="top:2334px">Sed ut perspiciatis unde omnis iste natus error sit voluptatem accusantium doloremque laudantium, totam rem aperiam, eaque ipsa quae ab illo inventore veritatis et quasi architecto beatae vitae dicta sunt explicabo. Nemo enim ipsam voluptatem quia voluptas sit aspernatur aut odit aut fugit, sed quia consequuntur magni dolores eos qui ratione voluptatem sequi nesciunt.</p>
<p class="abs about-copy" style="top:2457px">Nemo enim ipsam voluptatem quia voluptas sit aspernatur aut odit aut fugit, sed quia consequuntur magni dolores eos qui ratione voluptatem sequi nesciunt.Neque porro quisquam est, qui dolorem ipsum quia dolor sit amet, consectetur, adipisci velit, sed quia</p>

<footer class="abs site-footer">
  <div class="abs footer-brand">Lumo Peak Advisory</div>
  <div class="abs footer-rule"></div>
  <div class="abs contact" style="left:108px">
    <div class="contact-icon"><svg width="16" height="20" viewBox="0 0 16 20"><path d="M8 0a7 7 0 0 0-7 7c0 5 7 13 7 13s7-8 7-13a7 7 0 0 0-7-7z" fill="#fff"/><circle cx="8" cy="7" r="2.6" fill="#10294a"/></svg></div>
    <div><h4>Address :</h4><p>4712 SE 215 Avenue Miami FL 33190</p></div>
  </div>
  <div class="abs contact" style="left:502px">
    <div class="contact-icon"><svg width="20" height="16" viewBox="0 0 20 16" fill="none" stroke="#fff" stroke-width="2"><rect x="1" y="1" width="18" height="14" rx="2"/><path d="M1 3l9 6 9-6"/></svg></div>
    <div><h4>Email</h4><p>wilma82dun@postnest.example</p></div>
  </div>
  <div class="abs contact" style="left:855px">
    <div class="contact-icon"><svg width="18" height="18" viewBox="0 0 24 24"><path d="M6.6 10.8a15 15 0 0 0 6.6 6.6l2.2-2.2a1 1 0 0 1 1-.25 11.4 11.4 0 0 0 3.6.57 1 1 0 0 1 1 1V20a1 1 0 0 1-1 1A17 17 0 0 1 3 4a1 1 0 0 1 1-1h3.5a1 1 0 0 1 1 1c0 1.25.2 2.45.57 3.6a1 1 0 0 1-.25 1z" fill="#fff"/></svg></div>
    <div><h4>Phone</h4><p>Mobile : (000)-555-0142</p></div>
  </div>
  <p class="abs copyright">© Copyrights 2018 Lumo Peak Advisory.All Rights Reserved.</p>
</footer>

</body>
</html>
```